Modern Banner and Window Decal Design For Law Firm Lawyer

We are looking for three modern and sophisticated banner design and window decal for our law firm.

Banner measurements/types:

1) Height: 130 cm Width: 160 cm (Outdoor banner)
2) Height: 200 cm Width: 85 cm (Pull up/retractable indoor banner)

Window Decal:
3) Height: 70cm width 70cm

Our law firm is based in Melbourne, Australia and we deal with property law mostly.

We prefer a white background with classic text in black or grey. We would also like a dash of colour so please use a green, blue or aqua colour palette that is consistent with our logo. Vector attached. A nice photo of property, Melbourne city viee, or family home would be nice.

We do not want any law related images - scales of justice, gavel or the like.

Our ultimate goal is to communicate that the firm is modern, professional and knowledgeable

We would like the following:

1. Our logo
2. Our services: - Property Law - Wills - Powers of Attorney - Probate - Estate Administration - Consultancy & Agency
3. Phone number
4. Web Address

5. For pull up/retractable banner we would also like the following text:

We use the latest digital technology and fixed-fees to provide fast and affordable legal advice that is easy to understand.

For privacy reasons, we will provide business details once we have decided on the winner.

We will monitor entries closely and promise to provide feedback and guidance on each entry.

Thank you very much for considering this project.

Target Market(s)

General public, professionals, lawyers and conveyancers

Industry/Entity Type

Law Firm

Font styles to use
Sans Serif

Colors
0393ce
34a6d7
0456a4
3176b5
acd037
33b8a4
86cfc6
00a990
9ccb3b

Requirements
Must have
• 1. Our logo
• 2. Our services: - Property Law - Wills - Powers of Attorney - Probate & Estate Administration - Consultancy & Agency
• 3. Phone number
• 4. Web Address
Nice to have
• Picture of Melbourne, Australia city ; property/buildings/lawyers
Should not have
• We do not want any law related images - scales of justice, gavel or the like.

```html
<!DOCTYPE html>
<html lang="en">
<head>
<meta charset="utf-8">
<title>Ridgeline Lawyers – Banner Set</title>
<link href="https://fonts.googleapis.com/css2?family=Montserrat:wght@400;500&display=swap" rel="stylesheet">
<style>
  :root {
    --ink: #4a4a4d;
    --accent: #34a6d7;
    --accent-deep: #0393ce;
    --stage: #e6e8eb;
    --paper: #ffffff;
    --glass-light: #dfe9f3;
    --glass-mid: #8fb3d6;
    --glass-dark: #3f6f9e;
  }
  * { box-sizing: border-box; margin: 0; padding: 0; }
  html, body { width: 1200px; height: 1200px; overflow: hidden; }
  body {
    background: var(--stage);
    font-family: "Montserrat", Arial, sans-serif;
    color: var(--ink);
    position: relative;
  }

  /* Shared pieces */
  .brand {
    display: flex;
    align-items: center;
    justify-content: center;
    gap: 22px;
  }
  .brand-dot {
    border-radius: 50%;
    background: var(--accent);
    flex: none;
  }
  .brand-name {
    font-weight: 500;
    color: var(--ink);
    letter-spacing: 0.02em;
    line-height: 1.05;
  }
  .service-dot {
    display: inline-block;
    border-radius: 50%;
    background: var(--accent);
  }
  .contact { color: var(--accent-deep); font-weight: 500; }
  .building-photo {
    position: absolute;
    left: 0; right: 0; bottom: 0;
    background:
      linear-gradient(to bottom, var(--paper) 0%, rgba(255,255,255,0) 30%),
      linear-gradient(115deg, var(--glass-mid) 0%, var(--glass-dark) 45%, var(--glass-mid) 60%, var(--glass-light) 100%);
  }

  /* Outdoor banner */
  .outdoor-banner {
    position: absolute;
    left: 30px; top: 300px;
    width: 730px; height: 594px;
    background: var(--paper);
    box-shadow: 0 2px 10px rgba(0,0,0,0.12);
    overflow: hidden;
  }
  .outdoor-banner .brand { margin-top: 24px; height: 170px; }
  .outdoor-banner .brand-dot { width: 120px; height: 120px; }
  .outdoor-banner .brand-name { font-size: 50px; }
  .outdoor-banner .services {
    text-align: center;
    margin-top: 22px;
    line-height: 1.55;
  }
  .outdoor-banner .services p { font-size: 28px; }
  .outdoor-banner .services p.wide { font-size: 23px; }
  .outdoor-banner .service-dot { width: 9px; height: 9px; margin: 0 12px; vertical-align: middle; }
  .outdoor-banner .contacts {
    display: flex;
    justify-content: center;
    gap: 56px;
    margin-top: 14px;
    font-size: 29px;
  }
  .outdoor-banner .building-photo { height: 205px; }

  /* Pull-up banner */
  .pullup-banner {
    position: absolute;
    left: 810px; top: 80px;
    width: 360px; height: 1040px;
    background: var(--paper);
    box-shadow: 0 2px 10px rgba(0,0,0,0.12);
    overflow: hidden;
  }
  .pullup-banner .brand { margin-top: 28px; gap: 16px; }
  .pullup-banner .brand-dot { width: 96px; height: 96px; }
  .pullup-banner .brand-name { font-size: 30px; }
  .pullup-banner .services {
    list-style: none;
    text-align: center;
    margin-top: 46px;
  }
  .pullup-banner .services li { font-size: 25px; line-height: 1.3; }
  .pullup-banner .services li.wide { font-size: 22px; }
  .pullup-banner .service-dot { width: 7px; height: 7px; margin: 5px 0; }
  .pullup-banner .contacts {
    text-align: center;
    margin-top: 24px;
    line-height: 1.55;
  }
  .pullup-banner .phone { font-size: 28px; display: block; }
  .pullup-banner .web { font-size: 25px; display: block; }
  .pullup-banner .tagline {
    margin: 26px 18px 0;
    font-size: 17px;
    line-height: 1.4;
    font-weight: 400;
    letter-spacing: 0.02em;
  }
  .pullup-banner .building-photo { height: 290px; }
</style>
</head>
<body>

  <section class="outdoor-banner">
    <div class="brand">
      <span class="brand-dot"></span>
      <div class="brand-name">RIDGELINE<br>LAWYERS</div>
    </div>
    <div class="services">
      <p>PROPERTY LAW<span class="service-dot"></span>WILLS</p>
      <p>POWERS OF ATTORNEY<span class="service-dot"></span>PROBATE</p>
      <p class="wide">ESTATE ADMINISTRATION<span class="service-dot"></span>CONSULTANCY &amp; AGENCY</p>
    </div>
    <div class="contacts">
      <span class="contact">03 5550 1942</span>
      <span class="contact">ridgelinelegal.com.au</span>
    </div>
    <div class="building-photo" role="img" aria-label="Photograph looking up at glass office towers in the city"></div>
  </section>

  <section class="pullup-banner">
    <div class="brand">
      <span class="brand-dot"></span>
      <div class="brand-name">RIDGELINE<br>LAWYERS</div>
    </div>
    <ul class="services">
      <li>PROPERTY LAW</li>
      <li><span class="service-dot"></span></li>
      <li>WILLS</li>
      <li><span class="service-dot"></span></li>
      <li>POWERS OF ATTORNEY</li>
      <li><span class="service-dot"></span></li>
      <li>PROBATE</li>
      <li><span class="service-dot"></span></li>
      <li class="wide">ESTATE ADMINISTRATION</li>
      <li><span class="service-dot"></span></li>
      <li class="wide">CONSULTANCY &amp; AGENCY</li>
    </ul>
    <div class="contacts">
      <span class="contact phone">03 5550 1942</span>
      <span class="contact web">ridgelinelegal.com.au</span>
    </div>
    <p class="tagline">We use the latest digital technology and fixed-fees to provide fast and affordable legal advice that is easy to understand.</p>
    <div class="building-photo" role="img" aria-label="Photograph looking up at a glass skyscraper against a pale sky"></div>
  </section>

</body>
</html>
```